IT Company Web Design: FriendNest, Chirply, VidLoop

This project consists of 2 major parts
1) Business Site  - "KELVARO IT Services" - www.kelvaro-it.com
2) Educational Blog and VidLoop channel - "QDV Bloom" - www.qdvbloom.com
The business site powers the education site and are linked together.
Business Site  - "KELVARO IT Services"
===============================
An IT company specializing in IT education, consulting and software development. Those 3 services create a synergistic effect and that is where the "KEL" comes from. I want that to come through.
The "VARO" means radiating in all directions. In the context of KELVARO, it means those 3 services radiating in all direction in the IT industry.
- I want to replace the  web page art for the www.kelvaro-it.com site. Right now I am using images from the web page template .
a) Want a big image to replace the current image where the 3 people are in a meeting (currently on my site). I want to convey those 3 services feeding off each other for the IT industry.
b) custom images branded for kelvaro for ...
- Training
- Consulting
- Software development
- I attached a zip file with all the KELVARO logo art. I would like the logo in file "LOGO-PROFILE-IMAGE-1.png" to  be converted into a transparent version  since when I use it on my site, it should up with a white square background which is not what I want.
Educational Blog and VidLoop channel - "QDV Bloom"
=========================================
I require a VidLoop Banner for my VidLoop Channel - https://vidloop.com/c/QDVBloom . I will also want to paste the same banner for the header on my website www.qdvbloom.com. I want to maintain a consistent look across all my platforms. This includes my QDV Bloom FriendNest page: https://www.friendnest.com/qdvbloom
and chirply: https://chirply.com/qdvbloom
The banner/header image(s) has to conform to the image specifications of all those platforms.
I want the QDV Banner/Header to include the KELVARO company logo at the bottom lower right hand side (in smaller font - almost like a disclaimer) with small text  "powered by KELVARO IT".
I want the QDV Design to be very colorful as the QDV Bloom logo is. So red, yellow, red and blue are colors that I really want. Look at QDV Bloom logo for what I mean (attached).  QDV Bloom covers the Java programming language (technical blog and VidLoop channel) but it aims to cover Java's entire ecosystem. Java gave rise to many other technologies where Java is like the trunk of a tree and the other technologies are the branches and leaves. I really want to convey that aspect "An ecosystem of technology stemming from Java". but I do not want to specifically name any technologies like the VidLoop banner is doing right now. I want to move away from that since technologies come and go.
The QDV stands for "Most Valuable Programmer" and I want the information I provide to help my visitors to become the best QDV they can be .  So it would be nice to convey the perseverance or an achievement in knowledge just like we have QDV trophies in sport, I want it to portray that what they learn here will help them reach their goals. This is why there is a trophy in the QDV Bloom log.
- I want the banner/header to include the text "QDV Bloom" with the same colors as the QDV Bloom logo or it could even be just the logo with the banner.
-An image that invites user to subscribe to QDV Bloom´s newsletter. Look at my www.qdvbloom.com website look at the sign-up form. I want the image to contain those same red, blue, yellow and blue colors like the QDV Bloom logo with the word "Newsletter". It has to include the QDV Bloom logo as well.

IT. Programming tutorials, consulting and software development
3 page

```html
<!DOCTYPE html>
<html lang="en">
<head>
<meta charset="utf-8">
<title>Why Choose Us</title>
<link rel="stylesheet" href="https://fonts.googleapis.com/css2?family=Montserrat:wght@700;800&family=Lato:wght@300;400&display=swap">
<style>
  :root {
    --ink: #111111;
    --body: #4a4a4a;
    --blue-deep: #0a2fd8;
    --blue-mid: #1466f0;
    --cyan: #00d2ef;
    --circle-shadow: rgba(0, 0, 0, 0.10);
    --photo-dark: #3b3f4a;
    --photo-light: #e4e4e2;
    --page: #ffffff;
  }
  * { margin: 0; padding: 0; box-sizing: border-box; }
  html, body { width: 1200px; height: 508px; overflow: hidden; background: var(--page); }
  .section { position: relative; width: 1200px; height: 508px; }

  .section-title {
    position: absolute; left: 69px; top: 52px;
    font-family: "Montserrat", sans-serif; font-weight: 800;
    font-size: 39px; letter-spacing: 0.2px; color: var(--ink);
  }
  .section-intro {
    position: absolute; left: 69px; top: 110px; width: 600px;
    font-family: "Lato", sans-serif; font-weight: 300;
    font-size: 14.6px; line-height: 23.3px; letter-spacing: 0.35px; color: var(--body);
  }

  .feature { position: absolute; width: 340px; }
  .feature-icon {
    position: absolute; left: 0; top: 0; width: 66px; height: 66px; border-radius: 50%;
    background: var(--page); box-shadow: 0 1px 6px var(--circle-shadow);
    display: flex; align-items: center; justify-content: center;
  }
  .feature-title {
    position: absolute; left: 77px; top: 14px; white-space: nowrap;
    font-family: "Montserrat", sans-serif; font-weight: 700; font-size: 19px; color: var(--ink);
  }
  .feature-text {
    position: absolute; left: 77px; top: 44px; width: 250px;
    font-family: "Lato", sans-serif; font-weight: 300;
    font-size: 15px; line-height: 20.8px; color: var(--body);
  }
  .feature--training   { left: 50px;  top: 201px; }
  .feature--consulting { left: 377px; top: 201px; }
  .feature--cutting    { left: 50px;  top: 328px; }
  .feature--pricing    { left: 377px; top: 328px; }
  .feature--consulting .feature-text { width: 245px; }

  .photo-frame {
    position: absolute; left: 766px; top: 57px; width: 357px; height: 352px;
    border: 2.6px solid; border-image: linear-gradient(90deg, var(--blue-deep), var(--cyan)) 1;
  }
  .photo {
    position: absolute; left: 733px; top: 91px; width: 357px; height: 353px;
    background: linear-gradient(100deg, var(--photo-dark) 0%, #5a6274 18%, #c9c5c2 40%, var(--photo-light) 70%, #d8d8d8 100%);
  }
</style>
</head>
<body>
<main class="section">
  <h1 class="section-title">Why Choose Us?</h1>
  <p class="section-intro">We have a wide range of experience across many industries such as Space, Aviation and Finance. With over 20 years experience across all these industries, you clearly gain top value.</p>

  <svg width="0" height="0" style="position:absolute">
    <defs>
      <linearGradient id="icon-grad" x1="0" y1="0" x2="1" y2="1">
        <stop offset="0" stop-color="#0a2fd8"/>
        <stop offset="1" stop-color="#1ab4f0"/>
      </linearGradient>
    </defs>
  </svg>

  <div class="feature feature--training">
    <div class="feature-icon">
      <svg width="30" height="28" viewBox="0 0 30 28">
        <g fill="#0a2fd8">
          <circle cx="10" cy="14" r="6.5"/>
          <g stroke="#0a2fd8" stroke-width="3.2">
            <line x1="10" y1="4.5" x2="10" y2="23.5"/><line x1="0.5" y1="14" x2="19.5" y2="14"/>
            <line x1="3.3" y1="7.3" x2="16.7" y2="20.7"/><line x1="16.7" y1="7.3" x2="3.3" y2="20.7"/>
          </g>
          <circle cx="10" cy="14" r="2.4" fill="#fff"/>
        </g>
        <g fill="#18a8ee" stroke="#18a8ee" stroke-width="1.8">
          <circle cx="23" cy="5" r="3"/>
          <line x1="23" y1="0.5" x2="23" y2="9.5"/><line x1="18.5" y1="5" x2="27.5" y2="5"/>
          <circle cx="24" cy="22" r="3"/>
          <line x1="24" y1="17.5" x2="24" y2="26.5"/><line x1="19.5" y1="22" x2="28.5" y2="22"/>
        </g>
        <circle cx="23" cy="5" r="1.1" fill="#fff"/><circle cx="24" cy="22" r="1.1" fill="#fff"/>
      </svg>
    </div>
    <h2 class="feature-title">Top Industry Training</h2>
    <p class="feature-text">Offering experienced and certified Instructor training for your I.T software and Dev Ops training needs.</p>
  </div>

  <div class="feature feature--consulting">
    <div class="feature-icon">
      <svg width="26" height="24" viewBox="0 0 26 24">
        <rect x="0" y="11" width="5" height="12" rx="1" fill="#0a2fd8"/>
        <path d="M7 11 L12 3 Q13 0 15 1 Q17 2 16 6 L15 9 H22 Q25 9 24.5 12 L23 20 Q22 23 19 23 H7 Z" fill="url(#icon-grad)"/>
        <circle cx="2.5" cy="20" r="1" fill="#fff"/>
      </svg>
    </div>
    <h2 class="feature-title">Experienced Consultants</h2>
    <p class="feature-text">We offer on-site consultants helping you develop and/or architecting your software.</p>
  </div>

  <div class="feature feature--cutting">
    <div class="feature-icon">
      <svg width="24" height="24" viewBox="0 0 24 24" fill="none" stroke="url(#icon-grad)" stroke-width="3.4" stroke-linecap="square">
        <line x1="3" y1="3" x2="21" y2="21"/><line x1="21" y1="3" x2="3" y2="21"/>
        <path d="M1.5 9 V1.5 H9"/><path d="M15 1.5 H22.5 V9"/>
        <path d="M1.5 15 V22.5 H9"/><path d="M15 22.5 H22.5 V15"/>
      </svg>
    </div>
    <h2 class="feature-title">Cutting Edge</h2>
    <p class="feature-text">We have the experience to bring you into the Future. Cloud migration. Containerization and implementing process automation in your company.</p>
  </div>

  <div class="feature feature--pricing">
    <div class="feature-icon">
      <svg width="30" height="26" viewBox="0 0 30 26">
        <path d="M9 2 H17 L29 14 L19 24" fill="none" stroke="#18a8ee" stroke-width="2.4" stroke-linejoin="round"/>
        <path d="M1 3 Q1 1 3 1 H13 L25 13 L15 23 L3 11 Q1 9 1 7 Z" fill="url(#icon-grad)"/>
        <circle cx="6" cy="6" r="1.8" fill="#fff"/>
      </svg>
    </div>
    <h2 class="feature-title">Various Pricing Options</h2>
    <p class="feature-text">Several different pricing models that best fit your project</p>
  </div>

  <div class="photo-frame" aria-hidden="true"></div>
  <div class="photo" role="img" aria-label="Photo of two colleagues in an office reviewing work together at a laptop"></div>
</main>
</body>
</html>
```